【新商品の発売に合わせて商品に貼るラベルデザイン希望】
ターゲット:20代〜50代の女性/美と健康・ダイエットに興味ある人
キャッチコピー:「食べる程キレイになる究極の菌活スイーツ♡」
商品名:ミモリ花雪ジェラート/ドリンク
(デザインはどちらか一つでOK)
商品の特徴:甘酒や豆乳を使い完全無添加・無糖の甘くて美味しい、でも太るどころか食べる程に究極の菌活生活ができてキレイになるスイーツです。
※写真のスイーツのフローズンの部分だけをアイスにしてカップに入れます。
※ドリンクはそのフローズンが液体になっていて、透明のパックに入っています。
それらに貼るラベルのデザインをお願いします。
イメージ:キレイカッコいいか、京都の抹茶の商品を想像するようなシンプルで素朴な感じもOKです。

期待しています。宜しくお願い致します。

ターゲットの女性がそのラベルを見ただけでワクワクするもの。もしくは素朴感とか体に良いと言うのがイメージできるデザインを希望します。
【注記事項】
すみません、依頼したいのはロゴではなく、ラベル全体のデザインです。
勿論ロゴを入れて頂いてもいいですが、欲しいのはそのままラベルとして使えるデザインです。
質問がありましたので・・・

【甘酒のラベルのサイズです】
横7cm×縦12cm なのですが、これを上から被せるようにして折り曲げます。

前から見ると 7cm×7cmのラベル
裏面をみると、横7cm×縦5cm にちょっとした説明文や材料・製造元などを記載します。
ロゴではなく、背景も入れたそのままで使えるラベルを希望します。
裏面は背景だけでOK。

【アイス】
ルヴェロッサ位のサイズです。蓋だけでなく全体のデザインをお願いします。

どちらか出来れば、文字だけをかえてしようしますので、どちらでもOKです!

上手く記載出来てなくて申し訳ありません。
宜しくお願い致します。

珍しかったのと、素朴なイメージが気に入りました。
ありがとうございました

```html
<!DOCTYPE html>
<html lang="ja">
<head>
<meta charset="utf-8">
<title>ミモリ花雪ジェラート ドリンク ラベル</title>
<link rel="stylesheet" href="https://fonts.googleapis.com/css2?family=Noto+Serif+JP:wght@400;600;700&family=Cormorant+Garamond:wght@500&display=swap">
<style>
  :root{
    --pink:#e9b6c9;
    --cream:#f2eedb;
    --paper:#ffffff;
    --ink:#2f2f2f;
    --line:#3a3a3a;
    --accent:#e0457b;
    --badge:#e6739c;
    --ray:#d9d2b8;
  }
  *{margin:0;padding:0;box-sizing:border-box}
  html,body{width:700px;height:1200px;overflow:hidden;background:var(--cream)}
  .label{position:relative;width:700px;height:1200px;background:var(--cream);font-family:"Noto Serif JP",serif;color:var(--ink)}
  .label__top-band{position:absolute;left:0;top:0;width:700px;height:480px;background:var(--pink)}
  .label__rays{position:absolute;left:0;top:900px;width:700px;height:300px;
    background:radial-gradient(ellipse at 50% 100%, var(--ray) 0%, rgba(217,210,184,.35) 55%, rgba(242,238,219,0) 80%)}
  .label__frame{position:absolute;left:0;top:0}
  .label__back-text{position:absolute;left:0;width:700px;top:96px;text-align:center;transform:rotate(180deg);
    font-size:22px;letter-spacing:4px;line-height:1.7;color:var(--ink)}
  .label__ornament{position:absolute;left:230px;top:395px;width:240px;height:40px;
    background:linear-gradient(90deg,rgba(60,60,60,0),rgba(60,60,60,.35),rgba(60,60,60,0))}
  .label__brand{position:absolute;left:0;width:700px;top:440px;text-align:center;
    font-family:"Cormorant Garamond",serif;font-size:30px;letter-spacing:1px}
  .label__rule{position:absolute;left:140px;width:420px;border-top:2px solid var(--line)}
  .label__rule--top{top:492px}
  .label__rule--mid{top:572px}
  .label__rule--low{top:702px;left:150px;width:400px;border-top-width:1.5px}
  .label__catch{position:absolute;left:0;width:700px;text-align:center;font-weight:600;font-size:30px;letter-spacing:2px}
  .label__catch--1{top:500px}
  .label__catch--2{top:532px}
  .label__catch em{font-style:normal;color:var(--accent)}
  .label__name{position:absolute;left:150px;top:592px;width:400px;height:100px;display:flex;align-items:center;justify-content:center;gap:14px}
  .label__name-main{font-size:80px;font-weight:700;letter-spacing:4px;line-height:1}
  .label__name-sub{display:flex;flex-direction:column;font-weight:600;line-height:1.05}
  .label__name-sub span:first-child{font-size:26px;letter-spacing:1px}
  .label__name-sub span:last-child{font-size:50px;letter-spacing:4px}
  .label__wheat{position:absolute;top:600px;width:26px;height:100px;
    background:linear-gradient(180deg,rgba(90,90,90,.45),rgba(90,90,90,.15))}
  .label__wheat--left{left:108px}
  .label__wheat--right{left:566px}
  .label__tagline{position:absolute;left:0;width:700px;top:718px;text-align:center;font-size:32px;font-weight:600;letter-spacing:3px}
  .label__badge{position:absolute;left:498px;top:942px;width:124px;height:124px;border-radius:50%;background:var(--badge);
    color:#fff;display:flex;flex-direction:column;align-items:center;justify-content:center;font-weight:700;font-size:28px;line-height:1.2;letter-spacing:2px}
</style>
</head>
<body>
<div class="label">
  <div class="label__top-band"></div>
  <div class="label__rays" role="img" aria-label="下部から放射状に広がる細い光線模様"></div>

  <svg class="label__frame" width="700" height="1200" viewBox="0 0 700 1200" aria-hidden="true">
    <path d="M65,230 Q125,230 125,170 L125,150 C125,90 230,45 350,45 C470,45 575,90 575,150 L575,170 Q575,230 635,230
             L635,880 Q575,880 575,940 C575,1010 470,1050 350,1050 C230,1050 125,1010 125,940 Q125,880 65,880 Z"
          fill="var(--paper)" stroke="var(--line)" stroke-width="2"/>
  </svg>

  <div class="label__back-text">原材料・製造元<br>ここに記載します</div>

  <div class="label__ornament" role="img" aria-label="稲穂とリボンの飾り模様"></div>
  <div class="label__brand">Hana Yuki</div>

  <div class="label__rule label__rule--top"></div>
  <p class="label__catch label__catch--1">食べる程キレイになる</p>
  <p class="label__catch label__catch--2">究極の『<em>菌活スイーツ♥</em>』</p>
  <div class="label__rule label__rule--mid"></div>

  <div class="label__wheat label__wheat--left" role="img" aria-label="稲穂の飾り"></div>
  <div class="label__wheat label__wheat--right" role="img" aria-label="稲穂の飾り"></div>
  <h1 class="label__name">
    <span class="label__name-main">花雪</span>
    <span class="label__name-sub"><span>ミモリジェラート</span><span>ドリンク</span></span>
  </h1>
  <div class="label__rule label__rule--low"></div>

  <p class="label__tagline">甘酒・豆乳の自然の甘味。</p>

  <div class="label__badge"><span>無添加</span><span>無糖</span></div>
</div>
</body>
</html>
```